Dune Air & Plus business card

I need an awesome, double-sided business card designed with our new logo. I would like the one side black with the colored logo, and the back side is all yours. I'd like to see horizontal and vertical layouts. Get creative! Thank you.

Target Market(s)

HVAC, Heating and Cooling in Phoenix, AZ

Industry/Entity Type

HVAC

Contact Information for Business Card

We need our new logo on the card. Tom Harker, (623) 555-0142, tom@trydunesair.com, www.trydunesair.com, ROC 514273

```html
<!DOCTYPE html>
<html lang="en">
<head>
<meta charset="utf-8">
<title>Dune Air &amp; Plus — Business Card</title>
<link rel="stylesheet" href="https://fonts.googleapis.com/css2?family=Roboto:wght@400;700&family=Montserrat:wght@600&display=swap">
<style>
  :root {
    --page-bg: #f4f4f5;
    --card-bg: #17181d;
    --card-bg-edge: #101115;
    --brand-blue: #2a78d2;
    --brand-orange: #f3792b;
    --brand-red: #e0412a;
    --brand-amber: #f6a126;
    --text-light: #e6e7ea;
    --text-muted: #a9abb0;
  }
  * { box-sizing: border-box; margin: 0; padding: 0; }
  html, body {
    width: 800px; height: 1200px; overflow: hidden;
    background: var(--page-bg);
  }
  .sheet {
    width: 800px; height: 1200px;
    display: flex; flex-direction: column; align-items: center; justify-content: center;
    gap: 32px;
  }
  .card {
    position: relative;
    width: 640px; height: 366px;
    background: linear-gradient(135deg, var(--card-bg), var(--card-bg-edge));
    box-shadow: 0 2px 6px rgba(0,0,0,.25);
    overflow: hidden;
  }
  .brand-name {
    font-family: "Roboto", sans-serif;
    font-weight: 700;
    color: var(--brand-blue);
    white-space: nowrap;
    display: flex; align-items: center; gap: 10px;
  }
  .brand-dot {
    width: 14px; height: 14px; border-radius: 50%;
    background: var(--brand-orange);
    flex: none;
  }
  /* Front */
  .front .brand-block {
    position: absolute; left: 0; top: 0; width: 320px; height: 366px;
    display: flex; flex-direction: column; align-items: center; justify-content: center;
  }
  .front .brand-name { font-size: 27px; margin-top: -6px; }
  .license {
    position: absolute; left: 0; width: 320px; top: 258px;
    text-align: center;
    font-family: "Montserrat", sans-serif; font-weight: 600;
    font-size: 14px; color: var(--text-muted);
  }
  .divider {
    position: absolute; left: 319px; top: 83px;
    width: 2px; height: 200px;
    background: linear-gradient(180deg, var(--brand-red), var(--brand-amber));
  }
  .person-name {
    position: absolute; left: 362px; top: 76px;
    font-family: "Roboto", sans-serif; font-weight: 700;
    font-size: 35px; letter-spacing: .3px;
    background: linear-gradient(90deg, var(--brand-orange), var(--brand-red));
    -webkit-background-clip: text; background-clip: text; color: transparent;
  }
  .contact-list {
    position: absolute; left: 362px; top: 176px;
    list-style: none;
  }
  .contact-list::before {
    content: ""; position: absolute; left: 12px; top: 14px; width: 2px; height: 76px;
    background: var(--brand-blue);
  }
  .contact-item {
    position: relative;
    display: flex; align-items: center; gap: 10px;
    height: 26px; margin-bottom: 13px;
    font-family: "Roboto", sans-serif; font-size: 17.5px; color: var(--text-light);
  }
  .contact-icon {
    width: 26px; height: 26px; border-radius: 50%;
    background: var(--brand-blue);
    display: flex; align-items: center; justify-content: center; flex: none;
  }
  .contact-icon svg { width: 14px; height: 14px; }
  /* Back */
  .back { display: flex; align-items: center; justify-content: center; }
  .back .brand-name { font-size: 46px; gap: 14px; }
  .back .brand-dot { width: 22px; height: 22px; }
</style>
</head>
<body>
<main class="sheet">
  <section class="card front" aria-label="Card front">
    <div class="brand-block">
      <div class="brand-name"><span class="brand-dot"></span>Dune Air &amp; Plus</div>
    </div>
    <p class="license">ROC 514273</p>
    <div class="divider"></div>
    <h1 class="person-name">TOM HARKER</h1>
    <ul class="contact-list">
      <li class="contact-item">
        <span class="contact-icon">
          <svg viewBox="0 0 24 24" fill="#fff"><path d="M6.6 10.8a15 15 0 0 0 6.6 6.6l2.2-2.2a1 1 0 0 1 1-.25 11.4 11.4 0 0 0 3.6.57 1 1 0 0 1 1 1V20a1 1 0 0 1-1 1A17 17 0 0 1 3 4a1 1 0 0 1 1-1h3.5a1 1 0 0 1 1 1c0 1.25.2 2.45.57 3.57a1 1 0 0 1-.25 1z"/></svg>
        </span>
        (623) 555-0142
      </li>
      <li class="contact-item">
        <span class="contact-icon">
          <svg viewBox="0 0 24 24" fill="#fff"><path d="M3 5h18v14H3z M4 6.5v.5l8 5.5 8-5.5v-.5z" fill-rule="evenodd"/></svg>
        </span>
        tom@trydunesair.com
      </li>
      <li class="contact-item">
        <span class="contact-icon">
          <svg viewBox="0 0 24 24" fill="none" stroke="#fff" stroke-width="2"><circle cx="12" cy="12" r="9"/><path d="M3 12h18M12 3c3 3.5 3 14.5 0 18M12 3c-3 3.5-3 14.5 0 18"/></svg>
        </span>
        www.trydunesair.com
      </li>
    </ul>
  </section>

  <section class="card back" aria-label="Card back">
    <div class="brand-name"><span class="brand-dot"></span>Dune Air &amp; Plus</div>
  </section>
</main>
</body>
</html>
```